An innovative software company needs a business card!

We need a business card design for our new innovative software company. Please use the details for the business card provided in business card details section. We will use the business card paper like: https://www.plavex.com/us/products/nfc/business-cards-plus.html Our company name: kelvora We have already a logo and colors to use in business cards too ,

Target Market(s)

App & Sofware Development

Industry/Entity Type

Software

Contact Information for Business Card

Lukas Brenner, BSc.
Owner and Creative Superhero

Adress:
Tulpenweg 37/4/1809
A - 1100, Wien

Tel: +43 (0) 676 921 35 60
Email: lukas.brenner@kelvora.at
Web: www.kelvora.at

Requirements
Must have
• - Use our logo
Nice to have
• It would be nice to have a nice picture on the backside. (About apps, software, technicals or funy stuff) - Use our colors as in business card (optional)

```html
<!DOCTYPE html>
<html lang="en">
<head>
<meta charset="utf-8">
<title>kelvora – business card</title>
<link rel="stylesheet" href="https://fonts.googleapis.com/css2?family=Ubuntu:wght@400;500;700&display=swap">
<style>
  :root {
    --stage: #e9ecee;
    --card: #ffffff;
    --teal: #168fb4;
    --teal-deep: #0f7c9e;
    --brand: #1a9fd2;
    --swoosh: #c3c5c8;
    --ink-grey: #555a5f;
    --on-teal: #ffffff;
  }
  * { box-sizing: border-box; margin: 0; padding: 0; }
  html, body {
    width: 1200px; height: 1200px; overflow: hidden;
    background: var(--stage);
    font-family: "Ubuntu", sans-serif;
  }
  .sheet {
    position: relative; width: 1200px; height: 1200px;
    display: flex; flex-direction: column; align-items: center; justify-content: center; gap: 60px;
  }
  .card {
    position: relative; width: 900px; height: 514px;
    background: var(--card); overflow: hidden;
    box-shadow: 0 6px 22px rgba(0,0,0,.14);
  }
  .card__shapes { position: absolute; inset: 0; }

  /* contact panel */
  .address, .contacts {
    position: absolute; left: 30px; color: var(--on-teal);
    font-size: 16px; line-height: 1.5; list-style: none; white-space: nowrap;
  }
  .address { top: 40px; }
  .contacts { bottom: 36px; }
  .contacts li, .address li { display: flex; align-items: center; gap: 8px; }
  .address li + li { padding-left: 22px; }
  .icon { width: 14px; height: 14px; flex: none; }

  /* brand */
  .brand { position: absolute; display: flex; align-items: center; gap: 22px; color: var(--brand); }
  .brand__dot { border-radius: 50%; background: var(--brand); flex: none; }
  .brand__name { font-weight: 700; letter-spacing: -1px; line-height: 1; }
  .front .brand { left: 395px; top: 180px; }
  .front .brand__dot { width: 74px; height: 74px; }
  .front .brand__name { font-size: 104px; }

  .holder { position: absolute; left: 520px; top: 380px; }
  .holder__name { color: var(--brand); font-weight: 700; font-size: 34px; letter-spacing: -.5px; }
  .holder__role { color: var(--ink-grey); font-size: 21px; margin-top: 4px; padding-left: 40px; }

  /* back */
  .back .brand { left: 60px; top: 62px; gap: 14px; }
  .back .brand__dot { width: 46px; height: 46px; }
  .back .brand__name { font-size: 64px; }
  .artwork {
    position: absolute; left: 400px; top: 150px; width: 450px; height: 320px; border-radius: 14px;
    background: radial-gradient(circle at 35% 55%, #2f6fd8 0 28%, transparent 52%),
                linear-gradient(135deg, #f2a23a 0%, #e94b6a 30%, #8f4fd6 55%, #3aa7e8 78%, #5ccb4f 100%);
    opacity: .9;
  }
</style>
</head>
<body>
<main class="sheet">

  <section class="card front" aria-label="Card front">
    <svg class="card__shapes" viewBox="0 0 900 514" aria-hidden="true">
      <defs>
        <linearGradient id="panel" x1="0" y1="0" x2="1" y2="1">
          <stop offset="0" stop-color="var(--teal)"/>
          <stop offset="1" stop-color="var(--teal-deep)"/>
        </linearGradient>
      </defs>
      <path d="M0 0 H420 C 320 120, 290 300, 290 514 H0 Z" fill="url(#panel)"/>
      <path d="M420 0 C 320 120, 290 300, 290 514 H320 C 318 330, 350 150, 430 6 Z" fill="var(--swoosh)"/>
    </svg>

    <ul class="address">
      <li><svg class="icon" viewBox="0 0 14 14"><path d="M7 1 L13 6.5 H11 V13 H3 V6.5 H1 Z" fill="currentColor"/></svg>Tulpenweg 37/4/1809</li>
      <li>A - 1100, Wien</li>
      <li>Austria</li>
    </ul>

    <ul class="contacts">
      <li><svg class="icon" viewBox="0 0 14 14"><path d="M3 1 L5.5 1 L6.5 4 L5 5.2 C5.8 7 7 8.2 8.8 9 L10 7.5 L13 8.5 V11 C13 12 12 13 11 13 C5.5 12.5 1.5 8.5 1 3 C1 2 2 1 3 1 Z" fill="currentColor"/></svg>+43 (0) 676 921 35 60</li>
      <li><svg class="icon" viewBox="0 0 14 14"><rect x="1" y="3" width="12" height="8" fill="currentColor"/><path d="M1 3 L7 8 L13 3" stroke="var(--teal)" stroke-width="1.2" fill="none"/></svg>lukas.brenner@kelvora.at</li>
      <li><svg class="icon" viewBox="0 0 14 14"><circle cx="7" cy="7" r="6" fill="none" stroke="currentColor" stroke-width="1.4"/><path d="M1 7 H13 M7 1 C4 4 4 10 7 13 M7 1 C10 4 10 10 7 13" stroke="currentColor" stroke-width="1.1" fill="none"/></svg>www.kelvora.at</li>
    </ul>

    <div class="brand">
      <span class="brand__dot"></span>
      <span class="brand__name">kelvora</span>
    </div>

    <div class="holder">
      <p class="holder__name">LUKAS BRENNER</p>
      <p class="holder__role">Director</p>
    </div>
  </section>

  <section class="card back" aria-label="Card back">
    <div class="brand">
      <span class="brand__dot"></span>
      <span class="brand__name">kelvora</span>
    </div>
    <div class="artwork" role="img" aria-label="Illustration of a tablet with colourful app icons floating above its screen"></div>
  </section>

</main>
</body>
</html>
```